"Willow Drift" Mattress Pad Packaging

We need packaging for a mattress pad. This will be sold through retailers across North America. We need something modern and clean, an update from what we currently have. This is targeted towards older women. I've attached what our current packaging looks like as well as other mattress pad packaging. This is a simple product so we're open to creativity and experimentation. This is our first time using this site so we're very open and hoping for something fun.

Font styles to use
Serif
Sans Serif

Colors

Designer to choose colors to be used in the design.

```html
<!DOCTYPE html>
<html lang="en">
<head>
<meta charset="UTF-8">
<title>Willow Drift — Mattress Pad Label</title>
<link rel="stylesheet" href="https://fonts.googleapis.com/css2?family=Cinzel:wght@400;500&display=swap">
<style>
  :root {
    --backdrop: #dfe6e7;
    --label-green: #20502a;
    --pattern-green: #1a4423;
    --band-coral: #d88d6c;
    --cream: #f2dcc3;
  }
  html, body {
    margin: 0;
    padding: 0;
    width: 1200px;
    height: 901px;
    overflow: hidden;
    background: var(--backdrop);
  }
  .canvas {
    position: relative;
    width: 1200px;
    height: 901px;
  }
  .label {
    position: absolute;
    left: 220px;
    top: 112px;
    width: 760px;
    height: 676px;
    background: var(--label-green);
    overflow: hidden;
    font-family: "Cinzel", "Trajan Pro", serif;
    color: var(--cream);
    text-align: center;
    text-transform: uppercase;
  }
  .label-pattern {
    position: absolute;
    inset: 0;
    background: radial-gradient(ellipse at center, var(--label-green) 0%, var(--pattern-green) 100%);
  }
  .side-band {
    position: absolute;
    top: 0;
    width: 12px;
    height: 676px;
    background: var(--band-coral);
  }
  .side-band-left { left: 42px; }
  .side-band-right { right: 42px; }
  .brand-mark {
    position: absolute;
    left: 50%;
    top: 100px;
    width: 140px;
    height: 140px;
    margin-left: -70px;
    border-radius: 50%;
    background: var(--cream);
  }
  .brand-name {
    position: absolute;
    left: 0;
    right: 0;
    top: 293px;
    margin: 0;
    font-size: 40px;
    font-weight: 400;
    letter-spacing: 2px;
    line-height: 1;
  }
  .collection-name {
    position: absolute;
    left: 0;
    right: 0;
    top: 353px;
    margin: 0;
    font-size: 18px;
    letter-spacing: 4px;
    line-height: 1;
  }
  .divider {
    position: absolute;
    left: 180px;
    top: 416px;
    width: 400px;
    height: 2px;
    background: var(--cream);
  }
  .features {
    position: absolute;
    left: 0;
    right: 0;
    top: 458px;
    margin: 0;
    padding: 0;
    list-style: none;
    font-size: 20px;
    letter-spacing: 2.5px;
    line-height: 35px;
  }
</style>
</head>
<body>
<main class="canvas">
  <section class="label">
    <div class="label-pattern" role="img" aria-label="Repeating leaf-flower pattern in deep green tones"></div>

    <div class="side-band side-band-left" aria-hidden="true"></div>
    <div class="side-band side-band-right" aria-hidden="true"></div>

    <div class="brand-mark" aria-hidden="true"></div>
    <h1 class="brand-name">Willow Drift</h1>
    <p class="collection-name">Haute Collection</p>
    <div class="divider" aria-hidden="true"></div>
    <ul class="features">
      <li>300 Thread Count</li>
      <li>Stretch-to-Fit-Skirt</li>
      <li>Allergy Deterrent</li>
      <li>100% Cotton</li>
    </ul>
  </section>
</main>
</body>
</html>
```